Aesthetics Company Flyer (description of services)

We need a 5.5"x8.5" flyer describing the services we offer at velvet horizon aesthetics. We are an aesthetics company located in Conroe TX. Our products and services can be found at www.vhaesthetics-demo.com/services . We would like to see designs that are cohesive with our brand and website: https://www.vhaesthetics-demo.com/

```html
<!DOCTYPE html>
<html lang="en">
<head>
<meta charset="utf-8">
<title>Velvet Horizon Aesthetics – Services Flyer</title>
<link href="https://fonts.googleapis.com/css2?family=Poppins:wght@400;500;600;700;800&family=Kaushan+Script&family=Oswald:wght@600&display=swap" rel="stylesheet">
<style>
:root{
  --bg:#e9e8ea;
  --paper:#ffffff;
  --lilac:#b9a7d3;
  --lilac-deep:#a692c4;
  --lilac-soft:#ece4f5;
  --band:#ad9fc4;
  --ink:#1d1b20;
  --ink-soft:#3b3840;
  --photo-a:#ede7e2;
  --photo-b:#cfc6c0;
}
*{box-sizing:border-box;margin:0;padding:0}
html,body{width:1200px;height:1117px;overflow:hidden}
body{background:var(--bg);font-family:"Poppins",sans-serif;color:var(--ink);position:relative}
.page{position:absolute;top:141px;width:540px;height:835px;background:var(--paper);overflow:hidden;box-shadow:0 6px 18px rgba(0,0,0,.12)}
.page--front{left:40px}
.page--back{left:620px}
.abs{position:absolute}
.hero{position:absolute;left:0;top:0}
.brand{position:absolute;right:18px;top:28px;width:190px;text-align:center}
.brand__dot{width:96px;height:96px;border-radius:50%;background:var(--lilac-soft);border:2px solid var(--lilac);margin:0 auto 12px}
.brand__name{font-weight:500;font-size:15px;letter-spacing:3px;color:var(--ink-soft);line-height:1.5}
.tagline{left:20px;top:252px;width:496px;height:118px;border:2px solid var(--lilac);border-radius:12px;background:var(--paper);text-align:center;padding-top:10px}
.tagline__script{font-family:"Kaushan Script",cursive;color:var(--lilac-deep);font-size:24px;line-height:1.1}
.tagline__lead{font-weight:800;font-size:22px;line-height:1.15;margin-top:4px}
.lotus{left:28px;top:340px;width:92px;height:62px;border-radius:50%;background:radial-gradient(ellipse at 50% 40%,#fffdf5 0%,#f3efe4 55%,rgba(255,255,255,0) 75%)}
.services-title{left:0;right:0;top:392px;text-align:center;font-weight:800;font-size:25px;padding-left:20px}
.services-intro{left:40px;width:460px;top:432px;text-align:center;font-size:7.6px;line-height:1.45;color:var(--ink-soft)}
.section-tag{left:24px;top:484px;background:var(--lilac);color:#fff;font-weight:700;font-size:16px;padding:3px 12px}
.section-rule{left:150px;right:26px;top:508px;height:2px;background:var(--lilac)}
.iv-col{top:524px;width:228px}
.iv-col--left{left:28px}
.iv-col--right{left:292px;top:534px}
.iv-item{margin-bottom:10px}
.iv-item h3{font-weight:600;font-size:10.5px;margin-bottom:2px}
.iv-item p{font-size:7.4px;line-height:1.4;color:var(--ink-soft)}
.wash{left:-40px;bottom:-30px;width:380px;height:190px;background:radial-gradient(ellipse at 40% 70%,rgba(185,167,211,.45),rgba(185,167,211,0) 70%)}
.footer-curve{left:0;bottom:0}
.circles{top:212px;left:0;width:540px;height:165px}
.circle{position:absolute;top:0;width:160px;height:160px;border-radius:50%;border:3px solid var(--lilac);padding:5px;background:var(--paper)}
.circle span{display:block;width:100%;height:100%;border-radius:50%}
.treatments{left:14px;top:392px;width:516px;display:grid;grid-template-columns:1fr 1fr;column-gap:14px;row-gap:16px}
.treatment{display:flex;gap:10px;align-items:flex-start;min-height:86px}
.treatment__img{flex:0 0 64px;height:76px;border-radius:8px}
.treatment h3{font-weight:600;font-size:10px;margin-bottom:2px}
.treatment p{font-size:7.9px;line-height:1.35;color:var(--ink-soft)}
.contact{left:0;bottom:0;width:540px;height:96px}
.contact__row{position:absolute;left:40px;bottom:22px;display:flex;align-items:center;color:#fff}
.contact__phone{font-family:"Oswald",sans-serif;font-weight:600;font-size:30px;letter-spacing:.5px;display:flex;align-items:center;gap:10px}
.contact__divider{width:1px;height:34px;background:rgba(255,255,255,.8);margin:0 14px}
.contact__links{font-weight:600;font-size:11.5px;line-height:1.5}
.contact__links span{display:inline-block;width:7px;height:7px;border-radius:50%;border:1.5px solid #fff;margin-right:5px}
</style>
</head>
<body>

<!-- FRONT -->
<section class="page page--front">
  <svg class="hero" width="540" height="300" viewBox="0 0 540 300">
    <defs>
      <linearGradient id="heroFront" x1="0" y1="0" x2="1" y2="1">
        <stop offset="0" stop-color="var(--photo-a)"/><stop offset="1" stop-color="var(--photo-b)"/>
      </linearGradient>
    </defs>
    <path role="img" aria-label="Photo of a smiling woman relaxing during an IV hydration session" d="M0 0 H300 C352 80 350 200 262 300 H0 Z" fill="url(#heroFront)"/>
    <path d="M300 0 C352 80 350 200 262 300" fill="none" stroke="var(--lilac)" stroke-width="9"/>
  </svg>
  <div class="brand">
    <div class="brand__dot"></div>
    <div class="brand__name">VELVET HORIZON<br>AESTHETICS</div>
  </div>

  <div class="abs tagline">
    <div class="tagline__script">Everyone is beautiful.</div>
    <div class="tagline__lead">WITH US, EVERYONE CAN FEEL<br>BEAUTIFUL TOO</div>
  </div>
  <div class="abs lotus" role="img" aria-label="White lotus flower"></div>

  <h2 class="abs services-title">OUR SERVICES</h2>
  <p class="abs services-intro">At Velvet Horizon Aesthetics we offer a comprehensive list of aesthetic, skincare and weight loss services and IV hydration therapy. But before you embark on your journey with us, you must first book a consultation so we can assess and understand your needs and decide on the best option to address those needs.</p>

  <div class="abs section-tag">IV HYDRATION</div>
  <div class="abs section-rule"></div>

  <div class="abs iv-col iv-col--left">
    <div class="iv-item"><h3>Quench Hydrator</h3><p>Improves overall hydration status Dehydration<br>Acute illness</p></div>
    <div class="iv-item"><h3>Glutathione</h3><p>Decreases wrinkles and improves skin elasticity and hyperpigmentation, such as melasma / detoxification / protects cells against oxidative stress</p></div>
    <div class="iv-item"><h3>Myers' Cocktail</h3><p>Reduces Fatigue / Boosts immune system / Preventative therapy for Covid-19, Cold, &amp; Flu / Enhances Athletic Performance / Reduces Hangover symptoms</p></div>
    <div class="iv-item"><h3>Hangover</h3><p>Improves symptoms of being overserved Mineral Blend / B Vitamin complex / Ondansetron / Famotidine / Vitamin C / Glutathione / B12 (optional)</p></div>
    <div class="iv-item"><h3>Post Workout Recovery</h3><p>Post Athletic Event / Athletic Recovery / Any Recovery<br>Amino Blend / Mineral Blend / Vit C / Glutathione / Vit B complex / B1</p></div>
  </div>

  <div class="abs iv-col iv-col--right">
    <div class="iv-item"><h3>Migraine Rescue</h3><p>Research indicates that IV Magnesium is effective in reducing acute migraine attacks.</p></div>
    <div class="iv-item"><h3>Immunity Booster</h3><p>Strengthens, balances and heals immune system / Boosts immunity / protective for autoimmune conditions</p></div>
    <div class="iv-item"><h3>Flawless Glow</h3><p>Improves visible signs of aging, Wrinkles, Thinning hair, Hair loss, Thin, splitting, peeling nails</p></div>
    <div class="iv-item"><h3>Peak Athletic Performance</h3><p>Improves athletic performance / Increases activity tolerance</p></div>
    <div class="iv-item"><h3>NAD+</h3><p>Important in cell nuclear DNA repair<br>NAD and NAD+ occur naturally in your body<br>Play a major role in the chemical process of generating energy.<br>NAD+ is probably the most important co-factor for improving mitochondrial function.</p></div>
  </div>

  <div class="abs wash"></div>
  <svg class="abs footer-curve" width="540" height="40" viewBox="0 0 540 40">
    <path d="M0 18 C180 30 360 30 540 40 V40 H0 Z" fill="var(--lilac)"/>
  </svg>
</section>

<!-- BACK -->
<section class="page page--back">
  <svg class="hero" width="540" height="300" viewBox="0 0 540 300">
    <defs>
      <linearGradient id="heroBack" x1="0" y1="0" x2="1" y2="1">
        <stop offset="0" stop-color="var(--photo-a)"/><stop offset="1" stop-color="var(--photo-b)"/>
      </linearGradient>
      <radialGradient id="washBack" cx=".7" cy=".35" r=".55">
        <stop offset="0" stop-color="var(--lilac)" stop-opacity=".45"/><stop offset="1" stop-color="var(--lilac)" stop-opacity="0"/>
      </radialGradient>
    </defs>
    <rect x="250" y="0" width="290" height="300" fill="url(#washBack)"/>
    <path role="img" aria-label="Photo of a client in a robe receiving an IV drip from a nurse" d="M0 0 H300 C352 80 350 200 262 300 H0 Z" fill="url(#heroBack)"/>
    <path d="M300 0 C352 80 350 200 262 300" fill="none" stroke="var(--lilac)" stroke-width="9"/>
  </svg>
  <div class="brand" style="top:40px">
    <div class="brand__dot"></div>
    <div class="brand__name">VELVET HORIZON<br>AESTHETICS</div>
  </div>

  <div class="abs circles">
    <div class="circle" style="left:6px"><span role="img" aria-label="Portrait of a woman touching her face" style="background:linear-gradient(135deg,#e9d3c3,#c9a993)"></span></div>
    <div class="circle" style="left:190px"><span role="img" aria-label="Close-up portrait with glowing skin" style="background:linear-gradient(135deg,#7f9bb3,#c89b7b)"></span></div>
    <div class="circle" style="left:374px"><span role="img" aria-label="Smiling woman with smooth skin" style="background:linear-gradient(135deg,#e7c7b1,#c79a80)"></span></div>
  </div>

  <div class="abs treatments">
    <div class="treatment"><div class="treatment__img" role="img" aria-label="Weight loss injection pen" style="background:linear-gradient(135deg,#e2a675,#cfc9c4)"></div><div><h3>Weightloss</h3><p>Semaglutide stimulates insulin to be released from the pancreas inan effort to slow down gastric emptying and inhibits inappropriate release of sugars after we eat.</p></div></div>
    <div class="treatment"><div class="treatment__img" role="img" aria-label="Facial treatment in progress" style="background:linear-gradient(135deg,#f1ece8,#d8cdc5)"></div><div><h3>Fibrin Growth Factor (FGF)</h3><p>Fibrin Growth Factor (FGF) facial treatment enhances skin rejuvenation, scar and wound rejuvenation, and hair restoration by injecting plasma rich fibrin into the face.</p></div></div>
    <div class="treatment"><div class="treatment__img" role="img" aria-label="Wrinkle relaxer injection" style="background:linear-gradient(135deg,#e8e4e2,#8b7565)"></div><div><h3>Neurotoxin (Wrinkle Relaxer)</h3><p>Neurotoxin injections lessens facial lines that can give you a tired appearance. These lines are produced by repeatedmuscle contractions most noticeable on the forehead, between the eyebrows and around the eyes.</p></div></div>
    <div class="treatment"><div class="treatment__img" role="img" aria-label="Dermal filler treatment" style="background:linear-gradient(135deg,#3fa3d6,#d9a58e)"></div><div><h3>Dermal Fillers</h3><p>Dermal filler treatments plump up smile and frown lines, thin lips, and decrease cheek wrinkles and chin folds with FDA-approved volumizing hyaluronic acid, thus allow skin to restore fullness from the inside out.</p></div></div>
    <div class="treatment"><div class="treatment__img" role="img" aria-label="Microneedling treatment" style="background:linear-gradient(135deg,#4a4e8a,#e3c2ac)"></div><div><h3>GlideNeedle®</h3><p>GlideNeedle® is a microneedling treatment that generates the skin's self-repair mechanism and activates collagen and elastin production.</p></div></div>
    <div class="treatment"><div class="treatment__img" role="img" aria-label="Chemical peel application" style="background:linear-gradient(135deg,#e1c54a,#3a3a3a)"></div><div><h3>Chemical Peels</h3><p>Chemical Peels improve skin texture correcting pigmentation concerns, sun damage, and scarring.</p></div></div>
  </div>

  <div class="abs contact">
    <svg width="540" height="96" viewBox="0 0 540 96" style="position:absolute;left:0;top:0">
      <path d="M0 10 C60 0 120 0 170 2 L540 30 V96 H0 Z" fill="var(--band)"/>
      <path d="M0 0 C60 -6 120 -4 170 2 L0 10 Z" fill="var(--lilac-soft)"/>
    </svg>
    <div class="contact__row">
      <div class="contact__phone">
        <svg width="26" height="26" viewBox="0 0 26 26"><circle cx="13" cy="13" r="13" fill="#fff"/><path d="M8.5 6.5c.6-.4 1.4-.3 1.8.3l1.3 2c.3.5.2 1.2-.2 1.6l-.8.7c.7 1.6 1.8 2.8 3.4 3.6l.7-.8c.4-.5 1.1-.6 1.6-.2l2 1.3c.6.4.7 1.2.3 1.8l-.8 1.1c-.6.8-1.7 1.1-2.6.7C11.6 17.1 8.9 14.4 7.4 10.9c-.4-.9-.1-2 .7-2.6z" fill="var(--band)"/></svg>
        555 014 2290
      </div>
      <div class="contact__divider"></div>
      <div class="contact__links">
        <div><span></span>hello@vhaesthetics-demo.com</div>
        <div><span></span>www.vhaesthetics-demo.com</div>
      </div>
    </div>
  </div>
</section>

</body>
</html>
```